New Business Card Design Project

Looking for a modern business card design for an import distribution business for industrial technical products. The winning design will translate modern, sophistication, technical, professional and sustainable.

Target Market(s)

Technical customers

Industry/Entity Type

Business

Contact Information for Business Card

Dean Harlow
Sales Manager
M: 0471 625 183
P: 1300 872 619
dean@volkarsystems.com.au
4/18 Galloway Crest Road
Ashford Vale QLD 4521
www.volkarsystems.com.au

Font styles to use
Sans Serif

Colors
ec1f27
606060
000000
fbfbfb

Requirements
Must have
• My Logo which is the Volkar Systems logo attached
Nice to have
• Eurostile Bold font

```html
<!DOCTYPE html>
<html lang="en">
<head>
<meta charset="utf-8">
<title>Volkar Systems – Business Card</title>
<link rel="stylesheet" href="https://fonts.googleapis.com/css2?family=Michroma&family=Open+Sans:wght@400;600&display=swap">
<style>
  :root {
    --brand-red: #ec1f27;
    --steel-grey: #606060;
    --light-grey: #b9b9b9;
    --card-black: #0d0d0d;
    --ink-black: #000000;
    --paper-white: #fbfbfb;
    --canvas-bg: #e7e5e2;
  }
  * { box-sizing: border-box; margin: 0; padding: 0; }
  html, body {
    width: 1200px; height: 1023px; overflow: hidden;
    background: var(--canvas-bg);
  }
  .sheet {
    position: relative; width: 1200px; height: 1023px;
    display: flex; flex-direction: column; align-items: center; justify-content: center; gap: 50px;
  }
  .card {
    position: relative; width: 770px; height: 440px;
    border-radius: 34px; overflow: hidden;
    background: linear-gradient(160deg, #1c1c1c 0%, var(--card-black) 55%, var(--ink-black) 100%);
    box-shadow: 0 14px 30px rgba(0,0,0,.28);
  }

  /* Brand lockup */
  .brand {
    position: absolute; left: 60px; top: 58px;
    display: flex; align-items: center; gap: 18px;
    white-space: nowrap;
  }
  .brand-square { flex: 0 0 auto; width: 46px; height: 46px; background: var(--brand-red); }
  .brand-name {
    font-family: "Michroma", sans-serif; font-size: 40px; letter-spacing: 2px;
    color: var(--brand-red); line-height: 1; white-space: nowrap;
  }

  /* Front */
  .holder { position: absolute; left: 300px; top: 170px; }
  .holder-name {
    font-family: "Michroma", sans-serif; font-size: 25px; letter-spacing: 1px;
    color: var(--brand-red); white-space: nowrap;
  }
  .holder-role {
    margin-top: 8px;
    font-family: "Open Sans", sans-serif; font-size: 15px; letter-spacing: 1px;
    color: var(--light-grey);
  }
  .contact-list { list-style: none; margin-top: 16px; }
  .contact-item {
    display: flex; align-items: center; gap: 12px; margin-bottom: 7px;
    font-family: "Open Sans", sans-serif; font-size: 15px; color: var(--paper-white);
    white-space: nowrap;
  }
  .contact-icon {
    flex: 0 0 auto;
    width: 17px; height: 17px; background: var(--brand-red); border-radius: 2px;
    display: flex; align-items: center; justify-content: center;
  }
  .contact-icon svg { width: 11px; height: 11px; }
  .address {
    margin-top: 16px;
    font-family: "Open Sans", sans-serif; font-size: 14px; letter-spacing: .5px;
    color: var(--light-grey); line-height: 1.55; text-transform: uppercase;
    white-space: nowrap;
  }

  /* Back */
  .card--back .grid-texture {
    position: absolute; inset: 0;
    background: radial-gradient(ellipse at 55% 45%, #2a2a2a 0%, #141414 60%, #080808 100%);
  }
  .card--back .brand {
    left: 50%; top: 50%; transform: translate(-50%, -50%);
  }
  .card--back .brand-name { font-size: 42px; }
  .card--back .brand-square { width: 50px; height: 50px; }
</style>
</head>
<body>
<main class="sheet">

  <section class="card card--front" aria-label="Business card front">
    <div class="brand">
      <span class="brand-square"></span>
      <span class="brand-name">VOLKAR SYSTEMS</span>
    </div>

    <div class="holder">
      <h1 class="holder-name">DEAN HARLOW</h1>
      <p class="holder-role">SALES MANAGER</p>

      <ul class="contact-list">
        <li class="contact-item">
          <span class="contact-icon"><svg viewBox="0 0 12 12"><rect x="3" y="0.5" width="6" height="11" rx="1" fill="none" stroke="#fff" stroke-width="1.3"/><circle cx="6" cy="9.4" r=".8" fill="#fff"/></svg></span>
          0471 625 183
        </li>
        <li class="contact-item">
          <span class="contact-icon"><svg viewBox="0 0 12 12"><path d="M2.5 1 L4.6 1 L5.4 3.6 L4.1 4.6 Q5.2 7 7.4 8 L8.4 6.7 L11 7.5 L11 9.6 Q10.5 11 9 11 Q1 10 1 2.6 Q1 1 2.5 1 Z" fill="#fff"/></svg></span>
          1300 872 619
        </li>
        <li class="contact-item">
          <span class="contact-icon"><svg viewBox="0 0 12 12"><rect x="0.8" y="2.2" width="10.4" height="7.6" fill="none" stroke="#fff" stroke-width="1.2"/><path d="M1 2.6 L6 6.6 L11 2.6" fill="none" stroke="#fff" stroke-width="1.2"/></svg></span>
          dean@volkarsystems.com.au
        </li>
        <li class="contact-item">
          <span class="contact-icon"><svg viewBox="0 0 12 12"><circle cx="6" cy="6" r="5" fill="none" stroke="#fff" stroke-width="1.1"/><ellipse cx="6" cy="6" rx="2.2" ry="5" fill="none" stroke="#fff" stroke-width="1"/><path d="M1 6 H11" stroke="#fff" stroke-width="1"/></svg></span>
          www.volkarsystems.com.au
        </li>
      </ul>

      <p class="address">4/18 Galloway Crest Road<br>Ashford Vale QLD 4521</p>
    </div>
  </section>

  <section class="card card--back" aria-label="Business card back">
    <div class="grid-texture" role="img" aria-label="Dark tiled grid background pattern"></div>
    <div class="brand">
      <span class="brand-square"></span>
      <span class="brand-name">VOLKAR SYSTEMS</span>
    </div>
  </section>

</main>
</body>
</html>
```